New web design for a service provider in the medical field

We are looking for a new design for our website. We are a company that repairs and sells medical endoscopes. Our customers include doctors and hospitals. Our current website can be found at https://lumavend.de/en/lumavend-english.
We need a new web design (without programming) for the following 3 pages:
-Startpage https://lumavend.de/en/lumavend-english/
-Used endoscopes https://lumavend.de/en/used-endoscopes/
-Purchase https://lumavend.de/en/purchase/
The design should be modern and stylish.
The blue color of the logo should be reflected on the page, but not too intrusive.
I have uploaded the images from the header. If more images are needed, let me know and I will upload them.

Target Market(s)
Doctors and hospitals
Coding
Coded - Design and coding required
Number of Pages Required
1 page
Look and feel
Each slider illustrates characteristics of the customer's brand and the style your logo design should communicate.

```html
<!DOCTYPE html>
<html lang="en">
<head>
<meta charset="utf-8">
<title>Used Endoscopes – Lumavend</title>
<link href="https://fonts.googleapis.com/css2?family=Inter:wght@400;500;600;700&display=swap" rel="stylesheet">
<style>
:root{
  --blue:#29a3dc;
  --blue-dark:#1b7fb8;
  --navy:#243a52;
  --ink:#1d2630;
  --muted:#5d6b78;
  --pale:#eef5fb;
  --bar:#e9ecef;
  --brand-a:#0b4a8b;
  --brand-b:#e52d27;
  --brand-c:#0d0d0d;
  --white:#ffffff;
  --stage:#f4f5f7;
}
*{box-sizing:border-box;margin:0;padding:0}
html,body{width:1200px;height:2892px;overflow:hidden;background:var(--stage);font-family:"Inter",Arial,sans-serif;color:var(--ink)}
.page{position:absolute;left:229px;top:190px;width:742px;background:var(--white);box-shadow:0 10px 30px rgba(0,0,0,.18)}
section,header,nav,footer,.topbar{position:relative;width:742px;overflow:hidden}
.abs{position:absolute}
.topbar{height:23px;background:var(--bar);font-size:6px;color:var(--muted)}
.topbar .claim{left:42px;top:8px}
.topbar .links{left:475px;top:8px}
.topbar .lang{left:668px;top:6px;display:flex;gap:3px}
.topbar .lang span{padding:1px 3px}
.topbar .lang .on{background:var(--navy);color:var(--white)}
.site-header{height:72px;background:var(--white)}
.brand{left:52px;top:26px;display:flex;align-items:center;gap:6px;font-size:14px;font-weight:700;color:var(--navy)}
.brand i{width:10px;height:10px;border-radius:50%;background:var(--blue);display:block}
.contact-mail{left:400px;top:28px;display:flex;gap:6px;align-items:center;font-size:9px;color:var(--navy)}
.contact-phone{left:568px;top:22px;font-size:9px;color:var(--navy)}
.contact-phone small{display:block;font-size:5.5px;color:var(--muted);margin-top:2px}
.main-nav{height:33px;background:var(--blue);display:flex;font-size:6px;font-weight:600;color:var(--white);letter-spacing:.2px}
.main-nav span{position:absolute;top:13px}
.main-nav .active{background:rgba(255,255,255,.15);top:0;height:33px;padding:13px 10px 0;left:232px}
.hero{height:347px;background:var(--white)}
.hero-photo{left:300px;top:0;width:442px;height:300px;background:linear-gradient(90deg,#fff 0%,#e7ecf1 35%,#c9d2da 70%,#b3bec8 100%)}
.hero h1{left:60px;top:108px;font-size:24px;font-weight:400;line-height:1.35;color:var(--ink)}
.hero h1 b{color:var(--blue);font-weight:700;display:block}
.hero svg{left:0;bottom:0}
.intro{height:347px;background:var(--pale);overflow:visible;z-index:2}
.intro .copy{left:62px;top:38px;width:368px}
.intro h2{font-size:10px;font-weight:500;color:var(--blue);margin-bottom:10px}
.intro h2.second{margin-top:14px}
.intro p{font-size:6.6px;line-height:1.7;margin-bottom:8px;color:var(--ink)}
.help-card{left:465px;top:37px;width:205px;height:341px;background:var(--white);box-shadow:0 2px 10px rgba(0,0,0,.15);padding:40px 24px 0}
.help-card h3{font-size:10px;font-weight:500;color:var(--blue);margin-bottom:10px}
.help-card p{font-size:6.6px;line-height:1.8;margin-bottom:12px}
.help-photo{left:60px;bottom:0;width:145px;height:150px;background:linear-gradient(180deg,#f3f6f9,#dbe3ea)}
.features{height:390px;background:var(--blue)}
.feature{top:83px;width:173px;height:135px;background:var(--white);text-align:center;color:var(--blue);font-size:8px;padding-top:24px}
.feature svg{display:block;margin:0 auto 8px}
.feature small{display:block;font-size:5.5px;color:var(--ink);margin-top:4px;line-height:1.5}
.tagline{left:0;width:742px;top:283px;text-align:center;color:var(--white);font-size:23px;font-weight:500;line-height:1.5}
.product{height:287px}
.product .photo{top:0;height:287px}
.product h2{font-size:12px;font-weight:500;color:var(--white)}
.product p{font-size:6.6px;line-height:1.75;color:var(--white);margin-top:14px}
.brands{display:flex;gap:18px}
.brands span{display:block;width:100px;height:33px;color:var(--white);font-size:8px;font-weight:700;padding:12px 0 0 14px;letter-spacing:.3px}
.b-a{background:var(--brand-a)}.b-b{background:var(--brand-b)}.b-c{background:var(--brand-c)}
.outline-btn{display:inline-block;border:1px solid var(--white);background:var(--white);color:var(--blue);font-size:7.5px;padding:6px 10px;margin-top:24px}
.flexible{background:var(--blue)}
.flexible .photo{left:250px;width:492px;background:linear-gradient(90deg,var(--blue) 0%,#4a8fb8 40%,#3a5d7b 75%,#7d9bb5 100%)}
.flexible .text{left:73px;top:78px;width:220px}
.processors{background:var(--navy)}
.processors .photo{left:0;width:520px;background:linear-gradient(90deg,#5f7b96 0%,#4d6a86 45%,#2f4862 80%,var(--navy) 100%)}
.processors .text{right:77px;top:78px;width:240px;text-align:right}
.processors .brands{justify-content:flex-end}
.systems{background:var(--blue)}
.systems .photo{left:260px;width:482px;background:linear-gradient(90deg,var(--blue) 0%,#6cb6dd 45%,#b9d7e8 80%,#d6e5ee 100%)}
.systems .text{left:73px;top:78px;width:230px}
.accessories{background:var(--navy)}
.accessories .photo{left:0;width:520px;background:linear-gradient(90deg,#4e89ad 0%,#3f7296 45%,#2c4b66 80%,var(--navy) 100%)}
.accessories .text{right:77px;top:78px;width:260px;text-align:right}
.site-footer{height:150px;background:var(--navy);color:var(--white);font-size:6px}
.footer-links{left:78px;top:60px;display:flex;gap:20px}
.copyright{left:78px;top:96px;font-size:5.5px;color:#c6d0da}
.social{left:580px;top:58px;display:flex;gap:5px}
.social i{display:block;width:10px;height:10px;background:var(--white);border-radius:2px}
.badge{left:628px;top:52px;width:32px;height:30px;background:#f29a1f;border-radius:3px}
</style>
</head>
<body>
<div class="page">
  <div class="topbar">
    <span class="abs claim">Cause the outcome matters</span>
    <span class="abs links">Pickup Order &nbsp;|&nbsp; About Us &nbsp;|&nbsp; Contact Us</span>
    <span class="abs lang"><span>DE</span><span class="on">EN</span></span>
  </div>
  <header class="site-header">
    <div class="abs brand"><i></i>Lumavend</div>
    <div class="abs contact-mail">
      <svg width="16" height="11" viewBox="0 0 16 11"><rect x=".5" y=".5" width="15" height="10" fill="none" stroke="#29a3dc"/><path d="M.5 .5 8 6l7.5-5.5" fill="none" stroke="#29a3dc"/></svg>
      info@lumavend.de
    </div>
    <div class="abs contact-phone">+49 4151 555 010-0<small>Monday - Friday 08:00 - 20:00</small></div>
  </header>
  <nav class="main-nav">
    <span style="left:60px">HOME</span>
    <span style="left:128px">ENDOSCOPE REPAIR</span>
    <span class="active">USED ENDOSCOPE +</span>
    <span style="left:348px">ENDOSCOPE SYSTEM</span>
    <span style="left:462px">ENDOSCOPE ACCESSORIES +</span>
    <span style="left:610px">PURCHASE</span>
  </nav>
  <section class="hero">
    <div class="abs hero-photo" role="img" aria-label="Endoscope control bodies hanging in a storage cabinet"></div>
    <h1 class="abs">QUALITY WITHOUT<b>COMPROMISE</b></h1>
    <svg class="abs" width="742" height="90" viewBox="0 0 742 90">
      <path d="M0 20 L371 88 L742 20 V90 H0Z" fill="#eef5fb"/>
      <path d="M0 8 L371 80 L742 2 V8 L371 88 L0 20Z" fill="#e3f0f9"/>
      <path d="M120 30 L371 78 L640 22" fill="none" stroke="#1b7fb8" stroke-width="4"/>
    </svg>
  </section>
  <section class="intro">
    <div class="abs copy">
      <h2>Purchase of used endoscopes – the inexpensive alternative</h2>
      <p>Used endoscopes are an excellent, high-quality alternative to new equipment for all doctors and hospitals who want to add to their equipment pool cost-effectively. On our website you will find all types of equipment – gastroscopes, colonoscopes, bronchoscopes, cystoscopes and duodenoscopes.</p>
      <p>All used endoscopes that we offer for sale were already in medical use and have been professionally looked after and serviced during this time. In addition, we can offer you endoscopy accessories both for medical examinations and for cleaning and maintaining your endoscopes.</p>
      <h2 class="second">Quality with warranty for more safety</h2>
      <p>After the purchase, our technicians subjected the devices to extensive technical tests and overhauled them. Last but not least, we rely on well-known brands that themselves stand for a high quality standard – Orvana, Pellux and Fujara. For these reasons we can offer a twelve month warranty on our used equipment!</p>
      <p>Only tested quality leaves our company: To ensure the highest quality standards, we carry out an intensive outgoing inspection on every device before dispatch. We enclose documentation of the test result with your endoscope and archive it for future reference.</p>
    </div>
    <aside class="abs help-card">
      <h3>We'll help you!</h3>
      <p>Do you have any questions, would you like detailed advice or would you like to place an order?</p>
      <p>Our staff will be happy to assist you:</p>
      <p>+49 4151 555 010-0<br>info@lumavend.de<br>via contact form</p>
      <div class="abs help-photo" role="img" aria-label="Customer service agent wearing a headset"></div>
    </aside>
  </section>
  <section class="features">
    <div class="abs feature" style="left:73px">
      <svg width="30" height="30" viewBox="0 0 30 30"><circle cx="15" cy="15" r="13" fill="none" stroke="#1d2630" stroke-width="2"/><text x="15" y="18" font-size="9" font-weight="700" text-anchor="middle" fill="#1d2630" font-family="Inter,sans-serif">12</text></svg>
      12 months warranty<small>Highest quality standards</small>
    </div>
    <div class="abs feature" style="left:271px">
      <svg width="30" height="30" viewBox="0 0 30 30"><circle cx="15" cy="11" r="7" fill="#1b7fb8"/><path d="M3 29c0-7 5-11 12-11s12 4 12 11z" fill="#1d2630"/></svg>
      Best customer service<small>We are there for you – from<br>08:00 to 20:00!</small>
    </div>
    <div class="abs feature" style="left:469px">
      <svg width="30" height="30" viewBox="0 0 30 30"><path d="M15 2a8 8 0 0 0-8 8c0 6 8 14 8 14s8-8 8-14a8 8 0 0 0-8-8z" fill="#1b7fb8"/><circle cx="15" cy="10" r="3" fill="#fff"/><ellipse cx="15" cy="26" rx="10" ry="2.5" fill="none" stroke="#1d2630" stroke-width="1.5"/></svg>
      Worldwide shipping<small>Our service knows no borders!</small>
    </div>
    <div class="abs tagline">USED DEVICE - FAIR PRICE -<br>FULL PERFORMANCE</div>
  </section>
  <section class="product flexible">
    <div class="abs photo" role="img" aria-label="Flexible video endoscopes hanging in a clinic"></div>
    <div class="abs text">
      <h2>Flexible video endoscopes</h2>
      <p>Discover our flexible endoscopes from the best brands such as Orvana, Pellux and Fujara: gastroscopes, colonoscopes, bronchoscopes, duodenoscopes, cystoscopes and more.</p>
      <div class="brands" style="margin-top:28px"><span class="b-a">ORVANA ›</span><span class="b-b">PELLUX ›</span><span class="b-c">FUJARA ›</span></div>
    </div>
  </section>
  <section class="product processors">
    <div class="abs photo" role="img" aria-label="Endoscope processor and light source unit with cable"></div>
    <div class="abs text" style="width:360px">
      <h2>Processores and light-sources</h2>
      <p style="margin-left:120px">Provide better diagnosis to your patients by means of high-resolution imaging, implemented by the best video processors of the latest generation.</p>
      <div class="brands" style="margin-top:28px"><span class="b-a">ORVANA ›</span><span class="b-b">PELLUX ›</span><span class="b-c">FUJARA ›</span></div>
    </div>
  </section>
  <section class="product systems">
    <div class="abs photo" role="img" aria-label="Clinician working at an endoscopy system"></div>
    <div class="abs text">
      <h2>Endoscopy systems</h2>
      <p>We help you with configuring a complete endoscopy system for your needs and requirements – from the endoscope to the peripheral devices (processor, light source, screen, suction pump, etc.).</p>
      <span class="outline-btn">Learn all about endoscopy-system &nbsp;→</span>
    </div>
  </section>
  <section class="product accessories">
    <div class="abs photo" role="img" aria-label="Endoscope and accessories laid on a table"></div>
    <div class="abs text">
      <h2>Accesories</h2>
      <p>Cover your needs for consumables for single or multiple specific use – from biopsy forceps to cleaning brushes and much more.</p>
      <span class="outline-btn">Find your accesories here &nbsp;→</span>
    </div>
  </section>
  <footer class="site-footer">
    <div class="abs footer-links"><span>Informations</span><span>About Us</span><span>Contact Us</span><span>TOS</span><span>Copyrights</span><span>Privacy Policy</span></div>
    <div class="abs copyright">© 2022 Lumavend GmbH</div>
    <div class="abs social"><i></i><i></i></div>
    <div class="abs badge"></div>
  </footer>
</div>
</body>
</html>
```